Doggy Shampoo needs a shout-out Sticker design for its bottle

We need a front-and-back sticker design for our 500ml doggy shampoo bottle (bottle design attached). Bottle color has not been determined yet, but it will not be a clear bottle. Most likely white or other bright colors. This shampoo contains virgin coconut oil (VCO) and fruit extract for soft and shiny fur, and the formula is paraben-free for the health conscious. We want our bottle to stand out among others on store shelves.
Updates

Target Market(s)

Target buyers are social media conscious dog owners who cares about the appearance, happiness and health of their pets.

Industry/Entity Type

Pet Care

Colors

Designer to choose colors to be used in the design.

Requirements
Must have
• Logo/Brand as attached.
• Must mention that it contains Virgin Coconut Oil (VCO) and fruit extract for soft and shiny fur (wordings for the benefit can be modified).
• In the back sticker design, for ingredients, just put any 5 or 6 usual ingredients because it will probably be edited again and save space for barcode and QR Code.
Nice to have
• The cutout shape of the sticker is as enclosed.
Should not have
• We would prefer not to have photograph of a dog in the design because photographs are in most of pet products and our bottle will not stand out. Instead, you can provide a nice, fashionable or groovy drawing of a dog or dogs.

```html
<!DOCTYPE html>
<html lang="en">
<head>
<meta charset="utf-8">
<title>Mimo Pet Care Shampoo Label</title>
<link rel="stylesheet" href="https://fonts.googleapis.com/css2?family=Montserrat:wght@400;500;600;700;800&display=swap">
<style>
  :root {
    --teal: #74cdd3;
    --teal-deep: #5fb8bf;
    --silver-light: #f4f5f6;
    --silver-dark: #b9bcbf;
    --white: #ffffff;
    --orange: #d98e33;
    --ink: #2d4a4d;
    --page: #ffffff;
  }
  html, body {
    margin: 0;
    padding: 0;
    width: 721px;
    height: 1200px;
    overflow: hidden;
    background: var(--page);
  }
  .label {
    position: relative;
    width: 721px;
    height: 1200px;
    border-radius: 42px;
    overflow: hidden;
    background: var(--teal);
    font-family: "Montserrat", sans-serif;
  }
  .label__shapes {
    position: absolute;
    inset: 0;
  }
  .label__dog-art {
    position: absolute;
    left: 300px;
    top: 440px;
    width: 410px;
    height: 760px;
    border-radius: 180px 180px 0 0;
    background: radial-gradient(ellipse at 50% 35%, #cfe9eb 0%, #9fd6da 45%, var(--teal-deep) 100%);
    opacity: 0.85;
  }
  .brand {
    position: absolute;
    left: 40px;
    top: 62px;
    margin: 0;
    font-weight: 700;
    font-size: 76px;
    line-height: 1;
    color: var(--orange);
  }
  .product-name {
    position: absolute;
    left: 350px;
    top: 335px;
    margin: 0;
    transform: translate(-50%, -50%) rotate(-45deg);
    font-weight: 800;
    font-size: 132px;
    line-height: 1;
    color: var(--white);
    letter-spacing: 1px;
    white-space: nowrap;
    text-shadow: 4px 6px 10px rgba(40, 70, 75, 0.35);
  }
  .category {
    position: absolute;
    left: 560px;
    top: 295px;
    margin: 0;
    transform: translate(-50%, -50%) rotate(-45deg);
    font-weight: 400;
    font-size: 17px;
    letter-spacing: 20px;
    color: var(--ink);
    white-space: nowrap;
  }
  .claim {
    position: absolute;
    left: 64px;
    top: 722px;
    display: flex;
    align-items: center;
    gap: 30px;
    margin: 0;
    font-weight: 600;
    font-size: 21px;
    color: var(--orange);
  }
  .claim__marker {
    width: 22px;
    height: 22px;
    background: var(--orange);
    transform: rotate(45deg);
  }
  .hero-ingredient {
    position: absolute;
    left: 85px;
    top: 815px;
    margin: 0;
    font-weight: 600;
    font-size: 31px;
    line-height: 50px;
    color: var(--white);
  }
  .benefits {
    position: absolute;
    left: 85px;
    top: 1003px;
    margin: 0;
    padding: 0;
    list-style: none;
    font-weight: 400;
    font-size: 17px;
    line-height: 40px;
    color: var(--white);
    letter-spacing: 0.5px;
  }
  .volume {
    position: absolute;
    left: 85px;
    top: 1124px;
    margin: 0;
    font-weight: 400;
    font-size: 25px;
    color: var(--white);
  }
</style>
</head>
<body>
  <main class="label">
    <svg class="label__shapes" width="721" height="1200" viewBox="0 0 721 1200" aria-hidden="true">
      <defs>
        <linearGradient id="silverFill" x1="0" y1="0" x2="1" y2="1">
          <stop offset="0" stop-color="var(--silver-dark)"/>
          <stop offset="0.55" stop-color="var(--silver-light)"/>
          <stop offset="1" stop-color="#dfe1e3"/>
        </linearGradient>
        <linearGradient id="lightBand" x1="1" y1="0" x2="0" y2="1">
          <stop offset="0" stop-color="#ffffff" stop-opacity="0.85"/>
          <stop offset="0.5" stop-color="#ffffff" stop-opacity="0.35"/>
          <stop offset="1" stop-color="#ffffff" stop-opacity="0.15"/>
        </linearGradient>
      </defs>
      <polygon class="label__band" points="545,0 721,0 721,250 0,790 0,565" fill="url(#lightBand)"/>
      <polygon class="label__corner" points="0,0 548,0 186,372 0,206" fill="url(#silverFill)"/>
    </svg>

    <div class="label__dog-art" role="img" aria-label="Illustration of a seated pug puppy in teal tones"></div>

    <p class="brand">Mimo</p>
    <h1 class="product-name">SHAMPOO</h1>
    <p class="category">PET CARE</p>

    <p class="claim"><span class="claim__marker"></span>Paraben-free</p>

    <p class="hero-ingredient">Virgin<br>Coconut<br>Oil</p>

    <ul class="benefits">
      <li>LIME EXTRACT</li>
      <li>FUR SOFT ANY SHINY!</li>
    </ul>

    <p class="volume">10 fl.oz</p>
  </main>
</body>
</html>
```